Banner ad for www.brightquiver.example - Online Service for photographers

We need a simple and clean looking banner design that we can use in different formats and contexts online.

We're a new online service for photographers - providing websites, direct picture sales, media management, file delivery and cloud storage.

Our core message is 'Tools for Photographers': Sell Photos - Create Websites - Share Collections

Our target market is professional and 'serious amateur' photographers. We offer free 30 day trials. Members pay monthly or yearly subscriptions.

We're looking for something eye catching, graphically simple and modern that delivers the message clearly.

Required sizes are:

Leader board 728X90
Square pop up - 250x250
Wide skyscraper - 160x600
Button - 120x90
Updates

Target Market(s)

Our core target market is professional and serious amateur/enthusiast photographers.

Industry/Entity Type

Media

Requirements
Must have
• We need our logo

```html
<!DOCTYPE html>
<html lang="en">
<head>
<meta charset="utf-8">
<title>BrightQuiver – Tools for Photographers banners</title>
<link rel="stylesheet" href="https://fonts.googleapis.com/css2?family=Open+Sans:wght@400;600;700&display=swap">
<style>
  :root {
    --stage: #23272b;
    --stage-edge: #16191c;
    --panel-dark: #1c1c1c;
    --photo-light: #5a5a5a;
    --photo-dark: #1a1a1a;
    --white: #ffffff;
    --accent-orange: #f5a31a;
    --accent-red: #e2321c;
    --button-top: #ee4a2c;
    --button-bottom: #c92812;
    --ink: #3a3a3a;
    --ink-soft: #777777;
    --sky-top: #ffffff;
    --sky-bottom: #d6eaf8;
    --frame: #8a8f94;
  }
  * { margin: 0; padding: 0; box-sizing: border-box; }
  html, body { width: 1200px; height: 690px; overflow: hidden; }
  body {
    position: relative;
    font-family: "Open Sans", Arial, sans-serif;
    background: radial-gradient(ellipse at 50% 40%, var(--stage) 0%, var(--stage-edge) 100%);
    color: var(--white);
  }
  .banner { position: absolute; overflow: hidden; }
  .abs { position: absolute; }

  /* Square pop-up */
  .square {
    left: 421px; top: 77px; width: 358px; height: 357px;
    border-radius: 9px; border: 2px solid var(--frame); background: var(--white);
  }
  .square .photo-area {
    left: 0; top: 0; width: 100%; height: 269px;
    background: linear-gradient(135deg, var(--photo-light) 0%, #2c2c2c 45%, var(--photo-dark) 100%);
  }
  .headline { font-weight: 700; line-height: 1; letter-spacing: -0.5px; white-space: nowrap; }
  .headline small { font-size: 0.6em; font-weight: 600; letter-spacing: 0; }
  .square .headline { left: 24px; top: 20px; font-size: 36px; }
  .square .headline span { display: block; margin-bottom: 5px; }
  .rule { left: 0; top: 119px; width: 100%; height: 4px; display: flex; gap: 4px; }
  .rule i { flex: 1; }
  .rule i:nth-child(odd) { background: var(--accent-red); }
  .rule i:nth-child(even) { background: var(--accent-orange); }
  .features { list-style: none; }
  .features li { display: flex; align-items: center; font-weight: 600; white-space: nowrap; }
  .features svg { flex: none; }
  .square .features { left: 30px; top: 141px; font-size: 28px; }
  .square .features li { height: 35.5px; }
  .square .features svg { width: 24px; height: 24px; margin-right: 20px; }
  .pointer { left: 108px; top: 268px; width: 0; height: 0;
    border-left: 12px solid transparent; border-right: 12px solid transparent;
    border-top: 12px solid #222; }
  .cta {
    display: flex; align-items: center; justify-content: center; gap: 8px;
    color: var(--white); font-weight: 700; font-size: 18px;
    background: linear-gradient(var(--button-top), var(--button-bottom));
    border-radius: 3px; box-shadow: 0 1px 2px rgba(0,0,0,.3);
  }
  .cta::after { content: ""; border-left: 6px solid var(--white);
    border-top: 5px solid transparent; border-bottom: 5px solid transparent; }
  .square .cta { left: 16px; top: 288px; width: 141px; height: 50px; }
  .brand { display: flex; align-items: center; gap: 8px; color: var(--ink);
    font-weight: 600; white-space: nowrap; }
  .brand b { width: 20px; height: 20px; border-radius: 50%; background: var(--accent-orange); }
  .square .brand { left: 172px; top: 289px; font-size: 25px; }
  .url { color: var(--ink-soft); font-size: 13px; white-space: nowrap; }
  .square .url { left: 182px; top: 324px; }

  /* Leaderboard */
  .leader {
    left: 78px; top: 485px; width: 1038px; height: 129px;
    border-radius: 7px; border: 2px solid var(--frame); background: var(--panel-dark);
  }
  .leader .photo-left { left: 0; top: 0; width: 410px; height: 100%;
    background: linear-gradient(90deg, #3e3e3e 0%, #2a2a2a 60%, #454545 100%); }
  .leader .photo-feature { left: 410px; top: 0; width: 111px; height: 100%;
    background: linear-gradient(160deg, #e39a3c 0%, #b45d1f 45%, #3d2a1c 100%); }
  .leader .photo-mid { left: 521px; top: 0; width: 311px; height: 100%;
    background: linear-gradient(90deg, #262626 0%, #3a3a3a 70%, #505050 100%); }
  .leader .side-panel { left: 832px; top: 0; width: 206px; height: 100%;
    background: linear-gradient(var(--sky-top), var(--sky-bottom)); }
  .leader .headline { right: 661px; top: 22px; font-size: 40px; text-align: right; }
  .leader .headline span { display: block; margin-bottom: 6px; }
  .leader .features { left: 550px; top: 14px; font-size: 26px; }
  .leader .features li { height: 33px; }
  .leader .features svg { width: 23px; height: 23px; margin-right: 13px; }
  .leader .brand { left: 851px; top: 8px; font-size: 22px; }
  .leader .brand b { width: 18px; height: 18px; }
  .leader .cta { left: 866px; top: 43px; width: 139px; height: 49px; }
  .leader .url { left: 860px; top: 100px; }
</style>
</head>
<body>

<svg width="0" height="0" style="position:absolute" aria-hidden="true">
  <defs>
    <symbol id="icon-camera" viewBox="0 0 24 24">
      <rect x="1" y="5" width="22" height="16" rx="2" fill="#f5a31a"/>
      <rect x="7" y="2" width="8" height="4" rx="1" fill="#f5a31a"/>
      <circle cx="12" cy="13" r="5" fill="#222"/>
      <circle cx="12" cy="13" r="3" fill="#f5a31a"/>
    </symbol>
    <symbol id="icon-globe" viewBox="0 0 24 24">
      <circle cx="12" cy="12" r="11" fill="#f5a31a"/>
      <g fill="none" stroke="#222" stroke-width="1.4">
        <ellipse cx="12" cy="12" rx="4.5" ry="11"/>
        <line x1="1" y1="12" x2="23" y2="12"/>
        <path d="M3 6.5h18M3 17.5h18"/>
      </g>
    </symbol>
    <symbol id="icon-layers" viewBox="0 0 24 24">
      <path d="M12 13 1 18l11 5 11-5z" fill="#c97e10"/>
      <path d="M12 7 1 12l11 5 11-5z" fill="#e0920f"/>
      <path d="M12 1 1 6l11 5 11-5z" fill="#f5a31a"/>
    </symbol>
  </defs>
</svg>

<section class="banner square" aria-label="Square pop-up banner">
  <div class="abs photo-area" role="img" aria-label="Collage of black and white documentary photographs"></div>
  <h2 class="abs headline"><span>TOOLS <small>for</small></span><span>PHOTOGRAPHERS</span></h2>
  <div class="abs rule"><i></i><i></i><i></i><i></i><i></i></div>
  <ul class="abs features">
    <li><svg><use href="#icon-camera"/></svg>Sell photos</li>
    <li><svg><use href="#icon-globe"/></svg>Create websites</li>
    <li><svg><use href="#icon-layers"/></svg>Share collections</li>
  </ul>
  <div class="abs pointer"></div>
  <a class="abs cta">Try Us Free</a>
  <div class="abs brand"><b></b>BrightQuiver</div>
  <div class="abs url">www.brightquiver.example</div>
</section>

<section class="banner leader" aria-label="Leaderboard banner">
  <div class="abs photo-left" role="img" aria-label="Row of black and white documentary photographs"></div>
  <div class="abs photo-feature" role="img" aria-label="Colour wildlife photograph of a big cat"></div>
  <div class="abs photo-mid" role="img" aria-label="Faded black and white photograph"></div>
  <div class="abs side-panel"></div>
  <h2 class="abs headline"><span>TOOLS <small>for</small></span><span>PHOTOGRAPHERS</span></h2>
  <ul class="abs features">
    <li><svg><use href="#icon-camera"/></svg>Sell photos</li>
    <li><svg><use href="#icon-globe"/></svg>Create websites</li>
    <li><svg><use href="#icon-layers"/></svg>Share collections</li>
  </ul>
  <div class="abs brand"><b></b>BrightQuiver</div>
  <a class="abs cta">Try Us Free</a>
  <div class="abs url">www.brightquiver.example</div>
</section>

</body>
</html>
```